Bar and Grill needs specials signage

I have attached a file called "daily specials" I need it changed - so there is 1 sign/poster for each day/special
also attached other items to show some styling. I want the new posters chalkboard format, styled along the lines of the drink designs attached.
The designs should be scaleable, and editable, I will print locally

```html
<!DOCTYPE html>
<html lang="en">
<head>
<meta charset="UTF-8">
<title>Daily Specials – Chalkboard Posters</title>
<link rel="stylesheet" href="https://fonts.googleapis.com/css2?family=Amatic+SC:wght@700&family=Cabin+Sketch:wght@700&family=Kaushan+Script&family=Montserrat:wght@800;900&family=Playfair+Display:wght@900&display=swap">
<style>
  :root {
    --backdrop: #d1d2d4;
    --board: #1d1c1c;
    --chalk: #ececec;
    --chalk-soft: rgba(236,236,236,0.75);
    --orange: #f0712a;
    --green: #5fb08c;
    --teal: #36a49a;
    --pink: #ef7fb5;
    --yellow: #dcd97a;
    --peach: #f0cba8;
  }
  * { box-sizing: border-box; margin: 0; padding: 0; }
  html, body { width: 1200px; height: 1200px; overflow: hidden; }
  body { background: var(--backdrop); position: relative; }

  .poster {
    position: absolute; width: 364px; height: 497px;
    background: radial-gradient(ellipse at 50% 40%, #2a2929 0%, var(--board) 70%, #141313 100%);
    color: var(--chalk);
  }
  .poster__frame {
    position: absolute; inset: 14px 14px;
    border: 2px dashed var(--chalk-soft);
  }
  .poster__day {
    position: absolute; left: 49px; width: 267px; top: 54px; height: 44px;
    border: 1.5px solid var(--chalk-soft);
    font-family: "Playfair Display", Georgia, serif; font-weight: 900;
    font-size: 31px; letter-spacing: 3px; line-height: 41px; text-align: center;
    color: #cfcfcf;
  }
  .poster__day::after {
    content: ""; position: absolute; left: 10px; right: 10px; bottom: -7px;
    border-bottom: 1.5px solid var(--chalk-soft);
  }
  .line { position: absolute; left: 0; right: 0; text-align: center; line-height: 1; white-space: nowrap; }
  .caption { font-family: "Amatic SC", cursive; font-weight: 700; font-size: 31px; color: var(--chalk); }
  .sketch { font-family: "Cabin Sketch", cursive; font-weight: 700; }
  .script { font-family: "Kaushan Script", cursive; }
  .bold-sans { font-family: "Montserrat", Arial, sans-serif; font-weight: 900; }
  .art { position: absolute; border-radius: 50%; }
</style>
</head>
<body>

<!-- Monday -->
<section class="poster" style="left:46px; top:78px;">
  <div class="poster__frame"></div>
  <div class="poster__day">MONDAY</div>
  <div class="art" role="img" aria-label="Chalk drawing of a girl's head" style="left:38px; top:186px; width:56px; height:46px; background:var(--pink); opacity:.55;"></div>
  <div class="art" role="img" aria-label="Chalk drawing of a boy's head" style="left:272px; top:186px; width:56px; height:46px; background:var(--teal); opacity:.55;"></div>
  <div class="line sketch" style="top:184px; font-size:50px;"><span style="color:var(--pink)">KI</span><span style="color:var(--green)">DS</span></div>
  <div class="line sketch" style="top:248px; font-size:58px;"><span style="color:var(--pink)">EAT</span> <span style="color:var(--teal)">FREE</span></div>
  <div class="line caption" style="top:306px;">FROM OUR KIDS MENU,</div>
  <div class="line caption" style="top:343px;">WITH ADULT PURCHASE</div>
</section>

<!-- Tuesday wings -->
<section class="poster" style="left:424px; top:78px;">
  <div class="poster__frame"></div>
  <div class="poster__day">TUESDAY</div>
  <div class="line script" style="top:138px; font-size:40px; color:var(--green); padding-right:40px;">55 <span style="font-size:28px">cent.</span></div>
  <div class="line script" style="top:178px; font-size:34px; color:var(--orange); padding-left:110px;">wings</div>
  <div class="art" role="img" aria-label="Chalk drawing of a plate of wings" style="left:88px; top:220px; width:180px; height:122px; background:radial-gradient(ellipse, rgba(220,217,122,.45), rgba(220,217,122,.1));"></div>
  <div class="line caption" style="top:348px; font-size:34px;">AFTER 3:00 PM</div>
</section>

<!-- Wednesday -->
<section class="poster" style="left:802px; top:78px;">
  <div class="poster__frame"></div>
  <div class="poster__day">WEDNESDAY</div>
  <div class="line bold-sans" style="top:137px; font-size:38px; color:var(--orange); padding-right:60px;">STEAK</div>
  <div class="line script" style="top:168px; font-size:44px; color:var(--teal); padding-left:90px;">night</div>
  <div class="art" role="img" aria-label="Chalk drawing of a strip steak" style="left:98px; top:230px; width:192px; height:96px; border-radius:40%; background:radial-gradient(ellipse, rgba(240,203,168,.8), rgba(240,203,168,.3));"></div>
  <div class="line caption" style="top:335px;">HAND CUT STRIP STEAK,</div>
  <div class="line caption" style="top:370px;">POTATO AND SALAD</div>
</section>

<!-- Tuesday pizza -->
<section class="poster" style="left:42px; top:600px;">
  <div class="poster__frame"></div>
  <div class="poster__day">TUESDAY</div>
  <div class="line sketch" style="top:150px; font-size:34px; color:var(--orange);">PIZZA <span class="script" style="font-size:26px">and</span> WINGS</div>
  <div class="art" role="img" aria-label="Chalk drawing of a sliced pizza with a wing" style="left:94px; top:196px; width:184px; height:148px; background:radial-gradient(ellipse, rgba(240,113,42,.5), rgba(240,113,42,.12));"></div>
  <div class="line caption" style="top:350px; font-size:29px;">BUY ANY LARGE PIZZA AND GET</div>
  <div class="line caption" style="top:386px; font-size:29px;">10 BONELESS WINGS FREE</div>
</section>

<!-- Friday -->
<section class="poster" style="left:426px; top:600px;">
  <div class="poster__frame"></div>
  <div class="poster__day">FRIDAY</div>
  <div class="sketch" style="position:absolute; left:44px; top:218px; font-size:52px; color:var(--orange); transform:rotate(-62deg); transform-origin:left top;">FISH</div>
  <div class="bold-sans" style="position:absolute; left:154px; top:158px; font-size:22px;">AND</div>
  <div class="script" style="position:absolute; left:232px; top:150px; font-size:46px; color:var(--green); transform:rotate(55deg); transform-origin:left top;">chips</div>
  <div class="art" role="img" aria-label="Chalk drawing of a plate of fish and chips" style="left:114px; top:204px; width:144px; height:140px; background:radial-gradient(circle, rgba(240,113,42,.5), rgba(240,113,42,.12));"></div>
  <div class="line caption" style="top:356px;">BEER BATTERED COD FISH</div>
  <div class="line caption" style="top:392px;">AND STEAK FRIES</div>
</section>

<!-- Saturday -->
<section class="poster" style="left:806px; top:600px;">
  <div class="poster__frame"></div>
  <div class="poster__day">SATURDAY</div>
  <div class="line sketch" style="top:144px; font-size:22px; letter-spacing:4px; color:var(--orange);">"DUTCH OVEN"</div>
  <div class="line bold-sans" style="top:170px; font-size:16px; font-weight:800; color:var(--green);">BONELESS BEEF SHORT RIBS</div>
  <div class="line bold-sans" style="top:191px; font-size:16px; font-weight:800; color:var(--green);">CHIPOTLE BBQ</div>
  <div class="art" role="img" aria-label="Chalk drawing of a plated beef short rib" style="left:90px; top:224px; width:192px; height:96px; background:radial-gradient(ellipse, rgba(240,203,168,.8), rgba(240,203,168,.3));"></div>
  <div class="line caption" style="top:344px; font-size:29px;">SAUCE &amp; CRISPY ONIONS,</div>
  <div class="line caption" style="top:377px; font-size:29px;">GARLIC MASHED POTATOES,</div>
  <div class="line caption" style="top:409px; font-size:29px;">FRESH VEGETABLES</div>
</section>

</body>
</html>
```